Cards and Stationary for natural and holistic Earthing/Grounding products
Solvana Portugal
Cards and Stationary for natural and holistic Earthing/Grounding products - Health
Creative Brief
Bright & Fun-filled
Miro T. Kastelan, PhD
Solvana Portugal Founder
Rua dos Pinheiros Altos 14 2615-117, Valdoura, Portugal
info@solvanaportugal.pt
www.solvanaportugal.pt
The back of the card should incorporate the logo and web address.

```html
<!DOCTYPE html>
<html lang="en">
<head>
<meta charset="utf-8">
<title>Solvana Portugal – Business Card</title>
<link href="https://fonts.googleapis.com/css2?family=Open+Sans:wght@400;600;700&display=swap" rel="stylesheet">
<style>
  :root {
    --page-bg: #ecece8;
    --frame-green: #4f9a3a;
    --brand-green: #5a9e3f;
    --card-white: #ffffff;
    --text-grey: #6b6b6b;
    --divider: #c9c9c9;
  }
  * { margin: 0; padding: 0; box-sizing: border-box; }
  html, body {
    width: 1200px; height: 914px; overflow: hidden;
    background: var(--page-bg);
    font-family: "Open Sans", Arial, sans-serif;
  }
  .stage {
    width: 1200px; height: 914px;
    display: flex; align-items: center; justify-content: center;
  }
  .business-card {
    width: 1000px; height: 580px;
    background: var(--frame-green);
    padding: 30px;
    box-shadow: 0 10px 30px rgba(0,0,0,0.12);
  }
  .card-face {
    width: 100%; height: 100%;
    background: var(--card-white);
    display: flex; align-items: center;
    padding: 0 70px;
  }
  .brand-block {
    width: 380px;
    display: flex; align-items: center; gap: 16px;
  }
  .brand-dot {
    width: 46px; height: 46px; border-radius: 50%;
    background: var(--brand-green); flex-shrink: 0;
  }
  .brand-name {
    color: var(--brand-green);
    font-weight: 700; font-size: 34px; line-height: 1.1;
    white-space: nowrap;
  }
  .divider {
    width: 1px; height: 230px; background: var(--divider);
    margin-right: 30px; flex-shrink: 0;
  }
  .contact-block { color: var(--text-grey); }
  .person-name {
    color: var(--brand-green);
    font-weight: 700; font-size: 22px;
  }
  .person-title {
    font-size: 17px; margin-bottom: 22px;
  }
  .contact-list { list-style: none; }
  .contact-item {
    display: flex; align-items: flex-start; gap: 12px;
    font-size: 16px; line-height: 1.45; margin-bottom: 4px;
  }
  .contact-icon { width: 18px; height: 18px; flex-shrink: 0; margin-top: 3px; }
</style>
</head>
<body>
<main class="stage">
  <section class="business-card">
    <div class="card-face">
      <div class="brand-block">
        <span class="brand-dot"></span>
        <span class="brand-name">Solvana Portugal</span>
      </div>
      <div class="divider"></div>
      <div class="contact-block">
        <p class="person-name">Miro T. Kastelan, PhD</p>
        <p class="person-title">Solvana Portugal Founder</p>
        <ul class="contact-list">
          <li class="contact-item">
            <svg class="contact-icon" viewBox="0 0 18 18"><circle cx="9" cy="9" r="9" fill="#5a9e3f"/><path d="M9 4a3 3 0 0 0-3 3c0 2.3 3 6 3 6s3-3.7 3-6a3 3 0 0 0-3-3z" fill="#fff"/><circle cx="9" cy="7" r="1.1" fill="#5a9e3f"/></svg>
            <span>Rua dos Pinheiros Altos 14<br>2615-117, Valdoura, Portugal</span>
          </li>
          <li class="contact-item">
            <svg class="contact-icon" viewBox="0 0 18 18"><circle cx="9" cy="9" r="9" fill="#5a9e3f"/><path d="M6 4.5l1.6 0 .8 2.2-1 .9a6 6 0 0 0 2.9 2.9l.9-1 2.2.8v1.6c0 .6-.5 1.1-1.1 1.1A7.4 7.4 0 0 1 4.9 5.6c0-.6.5-1.1 1.1-1.1z" fill="#fff"/></svg>
            <span>+351 912 440 375</span>
          </li>
          <li class="contact-item">
            <svg class="contact-icon" viewBox="0 0 18 18"><circle cx="9" cy="9" r="9" fill="#5a9e3f"/><rect x="4.5" y="5.8" width="9" height="6.4" rx="0.8" fill="#fff"/><path d="M4.8 6.2L9 9.3l4.2-3.1" stroke="#5a9e3f" stroke-width="0.9" fill="none"/></svg>
            <span>info@solvanaportugal.pt</span>
          </li>
          <li class="contact-item">
            <svg class="contact-icon" viewBox="0 0 18 18"><circle cx="9" cy="9" r="9" fill="#5a9e3f"/><circle cx="9" cy="9" r="4.5" fill="none" stroke="#fff" stroke-width="1"/><ellipse cx="9" cy="9" rx="2" ry="4.5" fill="none" stroke="#fff" stroke-width="0.9"/><path d="M4.5 9h9" stroke="#fff" stroke-width="0.9"/></svg>
            <span>www.solvanaportugal.pt</span>
          </li>
        </ul>
      </div>
    </div>
  </section>
</main>
</body>
</html>
```